Vietnamese Restaurant Poster

We are a family restaurant specializing in Vietnamese comfort food of pho (Vietnamese Beef Noodle Soup).

We need to create a poster that will attract customers driving by our restaurant.

This poster will be placed on sandwich boards and placed on the intersecting streets.

We want it to be
- big and visually appealing.
- Preferably with a logo incorporating our name and a bowl of Pho
- a arrow sign pointing right
- our phone number 604-381-7295

The name of our restaurant is:

Pho Lanh Dao (Title text)
Vietnamese Restaurant (smaller text)

Reason: We have narrowed it down to 2  designs that we absolutely love. Thank you to all who have submitted.

Target Market(s)

Caucasian people who have not tried Vietnamese food. Our location is a little hidden so we want to make these posters to put on the main streets which will grab attention of people driving by to come into our restaurant

Industry/Entity Type

Restaurant

Requirements
Must have
• - big and visually appealing.
logo incorporating our name and a bowl of Pho
Nice to have
• a person eating a bowl of pho

```html
<!DOCTYPE html>
<html lang="en">
<head>
<meta charset="utf-8">
<title>Pho Lanh Dao – Vietnamese Restaurant Poster</title>
<link href="https://fonts.googleapis.com/css2?family=Poppins:wght@500;600&display=swap" rel="stylesheet">
<style>
  :root {
    --paper: #fff6ee;
    --cream: #fffbe8;
    --pale-yellow: #ffeb8a;
    --gold: #f8c52c;
    --orange: #f28a3c;
    --coral: #f0665a;
    --red: #e8372d;
    --deep-red: #cf2220;
    --blush: #f8b9aa;
    --ink: #0b0b0b;
    --logo-ink: #262626;
  }
  * { margin: 0; padding: 0; box-sizing: border-box; }
  html, body {
    width: 848px;
    height: 1200px;
    overflow: hidden;
    background: #ffffff;
  }
  .poster {
    position: relative;
    width: 848px;
    height: 1200px;
    overflow: hidden;
    font-family: "Poppins", Arial, sans-serif;
  }

  /* Food photo area: overhead table scene in warm tones */
  .food-scene {
    position: absolute;
    inset: 0;
    background:
      radial-gradient(ellipse 360px 260px at 100px 120px, #fffaf4 0%, rgba(255,250,244,0) 100%),
      radial-gradient(ellipse 300px 420px at 820px 120px, #fff3ec 0%, rgba(255,243,236,0) 100%),
      radial-gradient(ellipse 260px 200px at 120px 700px, #fde6dc 0%, rgba(253,230,220,0) 100%),
      radial-gradient(ellipse 330px 300px at 760px 560px, var(--coral) 0%, rgba(240,102,90,0) 100%),
      radial-gradient(ellipse 360px 300px at 760px 1140px, var(--red) 0%, rgba(232,55,45,0) 100%),
      linear-gradient(160deg, var(--paper) 0%, #fbd7c9 32%, var(--blush) 50%, var(--coral) 78%, var(--deep-red) 100%);
  }
  .food-scene .noodle-burst {
    position: absolute;
    left: 200px; top: 90px;
    width: 560px; height: 400px;
    border-radius: 50%;
    background: radial-gradient(ellipse at 55% 55%, var(--cream) 0%, var(--pale-yellow) 28%, var(--gold) 48%, rgba(242,138,60,0.6) 68%, rgba(242,138,60,0) 100%);
    transform: rotate(-18deg);
  }
  .food-scene .lime-dish {
    position: absolute;
    left: 40px; top: 445px;
    width: 240px; height: 200px;
    border-radius: 50%;
    background: radial-gradient(ellipse at 50% 50%, #fff07a 0%, var(--gold) 40%, rgba(240,102,90,0.7) 72%, rgba(240,102,90,0) 100%);
  }
  .food-scene .tea-cup {
    position: absolute;
    left: 445px; top: 650px;
    width: 150px; height: 140px;
    border-radius: 50%;
    background: radial-gradient(circle at 50% 50%, var(--coral) 0%, #f9c0b0 45%, var(--cream) 62%, rgba(248,185,170,0) 100%);
  }
  .food-scene .soup-bowl {
    position: absolute;
    left: 22px; top: 760px;
    width: 410px; height: 400px;
    border-radius: 50%;
    background: radial-gradient(circle at 52% 50%, var(--gold) 0%, var(--orange) 22%, var(--red) 52%, var(--deep-red) 86%, #f4a08c 94%, rgba(244,160,140,0) 100%);
  }

  .phone-number {
    position: absolute;
    left: 0;
    right: 0;
    top: 548px;
    text-align: center;
    font-weight: 600;
    font-size: 94px;
    letter-spacing: -2px;
    line-height: 1;
    color: var(--ink);
    text-shadow: 0 0 4px #ffffff, 0 0 8px rgba(255,255,255,0.85);
  }

  .brand {
    position: absolute;
    left: 526px;
    top: 940px;
    width: 252px;
    color: var(--logo-ink);
  }
  .brand-dot {
    display: block;
    width: 56px;
    height: 56px;
    margin: 0 auto 14px;
    border-radius: 50%;
    background: var(--red);
  }
  .brand-name {
    display: block;
    font-weight: 500;
    font-size: 33px;
    line-height: 1;
    text-align: center;
    white-space: nowrap;
  }
  .brand-tagline {
    display: block;
    margin-top: 6px;
    font-weight: 500;
    font-size: 8px;
    text-align: right;
  }
</style>
</head>
<body>
  <main class="poster">
    <div class="food-scene" role="img" aria-label="Motion-blurred overhead photo of a bowl of pho with beef, bean sprouts and herbs, chopsticks resting across it, a dish of lime and a cup of tea on a table, in warm red, orange and yellow tones">
      <span class="noodle-burst" aria-hidden="true"></span>
      <span class="lime-dish" aria-hidden="true"></span>
      <span class="tea-cup" aria-hidden="true"></span>
      <span class="soup-bowl" aria-hidden="true"></span>
    </div>
    <p class="phone-number">604-381-7295</p>
    <div class="brand">
      <span class="brand-dot"></span>
      <span class="brand-name">Pho Lanh Dao</span>
      <span class="brand-tagline">Vietnamese Restaurant</span>
    </div>
  </main>
</body>
</html>
```